Create Lanternfield HR Business Cards.

Create Business Cards for Lanternfield HR. 2 sided and Would like the back to have the logo.

Info for Business Card:
Address: 4827 Millbrook Ave Suite 230 Cleveland, Ohio 44987
Office Number: 216-555-0143
Mobile: 216-555-0192

Website: www.lanternfieldhr.example

Target Market(s)

Small to medium size businesses

Industry/Entity Type

Human Resources

Contact Information for Business Card

Company logo and information

Font styles to use
Serif
Sans Serif

Requirements
Must have
• Info for Business Card: Address: 4827 Millbrook Ave Suite 230 Cleveland, Ohio 44987 Office Number: 216-555-0143 Mobile: 216-555-0192 Website: www.lanternfieldhr.example

```html
<!DOCTYPE html>
<html lang="en">
<head>
<meta charset="utf-8">
<title>Lanternfield HR Business Cards</title>
<link href="https://fonts.googleapis.com/css2?family=Poppins:wght@400;600&display=swap" rel="stylesheet">
<style>
  :root {
    --backdrop: #e3e3e3;
    --card: #ffffff;
    --navy: #29235c;
    --orange: #f58a20;
  }
  html, body {
    margin: 0;
    padding: 0;
    width: 1200px;
    height: 1200px;
    overflow: hidden;
    background: var(--backdrop);
  }
  .sheet {
    position: relative;
    width: 1200px;
    height: 1200px;
    font-family: "Poppins", sans-serif;
    color: var(--navy);
  }
  .card {
    position: absolute;
    left: 190px;
    width: 786px;
    height: 472px;
    background: var(--card);
    overflow: hidden;
  }
  .card--front { top: 109px; }
  .card--back { top: 642px; }

  .ribbon {
    position: absolute;
    top: 0;
    width: 60px;
    height: 100%;
    background: linear-gradient(180deg,
      var(--navy) 0%, var(--navy) 18%,
      var(--orange) 30%, var(--navy) 42%,
      var(--orange) 56%, var(--navy) 68%,
      var(--orange) 80%, var(--navy) 90%, var(--navy) 100%);
  }
  .card--front .ribbon--left { left: 52px; }
  .card--front .ribbon--right { left: 674px; }
  .card--back .ribbon--inner { left: 583px; }
  .card--back .ribbon--outer { left: 674px; }

  .brand {
    position: absolute;
    left: 0;
    width: 786px;
    top: 208px;
    display: flex;
    align-items: center;
    justify-content: center;
    gap: 12px;
  }
  .brand__dot {
    width: 34px;
    height: 34px;
    border-radius: 50%;
    background: var(--orange);
  }
  .brand__name {
    font-weight: 600;
    font-size: 40px;
    color: var(--navy);
    letter-spacing: 0.5px;
  }

  .contact {
    position: absolute;
    left: 86px;
    top: 160px;
    margin: 0;
    padding: 0;
    list-style: none;
    font-size: 25px;
    line-height: 30px;
    font-weight: 400;
  }
  .contact__item {
    display: flex;
    align-items: center;
    gap: 8px;
    margin-bottom: 2px;
  }
  .contact__item--address { margin-top: 6px; }
  .contact__icon {
    flex: none;
    width: 24px;
    height: 24px;
  }
</style>
</head>
<body>
<main class="sheet">
  <section class="card card--front">
    <div class="ribbon ribbon--left" role="img" aria-label="Vertical band of repeating brand pattern in navy and orange"></div>
    <div class="ribbon ribbon--right" role="img" aria-label="Vertical band of repeating brand pattern in navy and orange"></div>
    <div class="brand">
      <span class="brand__dot"></span>
      <span class="brand__name">Lanternfield HR</span>
    </div>
  </section>

  <section class="card card--back">
    <ul class="contact">
      <li class="contact__item">
        <svg class="contact__icon" viewBox="0 0 24 24" aria-hidden="true">
          <circle cx="12" cy="12" r="11" fill="none" stroke="#29235c" stroke-width="1.5"/>
          <path d="M6 10 q6 -5 12 0 l-1.5 1.8 -2.5 -1 v-1.3 q-2 -0.8 -4 0 v1.3 l-2.5 1z" fill="#29235c"/>
          <rect x="7.5" y="12" width="9" height="5" rx="1" fill="#29235c"/>
          <circle cx="12" cy="14.5" r="1.3" fill="#fff"/>
        </svg>
        <span>216-555-0143</span>
      </li>
      <li class="contact__item">
        <svg class="contact__icon" viewBox="0 0 24 24" aria-hidden="true">
          <circle cx="12" cy="12" r="11" fill="none" stroke="#29235c" stroke-width="1.5"/>
          <path d="M8.5 6.5 l2 2.5 -1.2 1.5 q1.2 2.8 4.2 4.2 l1.5 -1.2 2.5 2 -1.5 2 q-6 -0.5 -9.5 -8.5z" fill="#29235c"/>
        </svg>
        <span>216-555-0192</span>
      </li>
      <li class="contact__item">
        <svg class="contact__icon" viewBox="0 0 24 24" aria-hidden="true">
          <circle cx="12" cy="12" r="11" fill="none" stroke="#29235c" stroke-width="1.5"/>
          <circle cx="12" cy="12" r="6.5" fill="none" stroke="#29235c" stroke-width="1"/>
          <ellipse cx="12" cy="12" rx="3" ry="6.5" fill="none" stroke="#29235c" stroke-width="1"/>
          <path d="M5.5 12 h13 M6.5 9 h11 M6.5 15 h11" stroke="#29235c" stroke-width="1"/>
        </svg>
        <span>www.lanternfieldhr.example</span>
      </li>
      <li class="contact__item contact__item--address">
        <svg class="contact__icon" viewBox="0 0 24 24" aria-hidden="true">
          <circle cx="12" cy="12" r="11" fill="none" stroke="#29235c" stroke-width="1.5"/>
          <path d="M12 18 q-4.5 -5 -4.5 -8 a4.5 4.5 0 0 1 9 0 q0 3 -4.5 8z" fill="#29235c"/>
          <circle cx="12" cy="10" r="1.6" fill="#fff"/>
        </svg>
        <span>4827 Millbrook Ave Suite<br>230 Cleveland, Ohio 44987</span>
      </li>
    </ul>
    <div class="ribbon ribbon--inner" role="img" aria-label="Vertical band of repeating brand pattern in navy and orange"></div>
    <div class="ribbon ribbon--outer" role="img" aria-label="Vertical band of repeating brand pattern in navy and orange"></div>
  </section>
</main>
</body>
</html>
```